QBrook718 Business Card Design

I am in need of a business card design.

Business Name: Harbor Stone 718 or Qbrook718 (we can try the business card with both variations)

I would like it to be somewhat different from the "average" business card

What do we do?

We link up with distributors of different items and we Market their products, sell their products, fulfill the shipment, and handle all customer service that goes along with it.

I will be uploading our logo as well as other business card ideas that i have seen and liked on the web.

I like the style of the "graphic design" business card that i uploaded. I was thinking maybe something like that but instead would read.

SYNC | SELL | SHIP

With maybe:
a computer or a Sync icon underneath SYNC
Some form of money sign underneath Sell
a delivery truck or something underneath SHIP.

And then I was thinking maybe put the logo on the back side like in the other business card that i uploaded.

I definitely want a double sided business card.

These are only my suggestions and if i was very confident in my idea then I wouldn't have to be on here. (So make what you think is nice because my opinion is probably not so great anyway!!)

Everything can be changed.

ALSO, For the logo
We can try and remove the text multi channel selling

For the Business card contact info:
Tom Haskins
CEO
2419 Pelkey Avenue
J7R-2B8
Montreal, Quebec

Thanks

Target Market(s)

Businesses

Industry/Entity Type

Information Technology

Font styles to use
Serif
Sans Serif
Decorative

Colors
34a6d6
33b8a4
aaaaaa
85cae6
33a6d7
0492cd
9d9d9d

Requirements
Must have
• Double Sided Business card
Nice to have
• Illustration graphics / Icons underneath the main points

```html
<!DOCTYPE html>
<html lang="en">
<head>
<meta charset="utf-8">
<title>Qbrook718 Business Card</title>
<link rel="stylesheet" href="https://fonts.googleapis.com/css2?family=Open+Sans:wght@400;700&family=Didact+Gothic&display=swap">
<style>
  :root {
    --page-bg: #ececec;
    --card-white: #ffffff;
    --band-grey: #8a8a8a;
    --brand-blue: #1a9ad6;
    --brand-green: #97c22b;
    --ink: #222222;
    --ink-soft: #333333;
  }
  * { margin: 0; padding: 0; box-sizing: border-box; }
  html, body {
    width: 942px; height: 1200px; overflow: hidden;
    background: var(--page-bg);
  }
  .canvas { position: relative; width: 942px; height: 1200px; }
  .card {
    position: absolute; left: 88px; width: 747px; height: 441px;
    background: var(--card-white);
    overflow: hidden;
    box-shadow: 0 2px 6px rgba(0,0,0,0.18);
  }
  .card-front { top: 122px; }
  .card-back { top: 626px; }

  /* Front */
  .brand {
    position: absolute; top: 0; left: 0; width: 100%; height: 243px;
    display: flex; align-items: center; justify-content: center; gap: 16px;
  }
  .brand-dot {
    width: 38px; height: 38px; border-radius: 50%;
    background: var(--brand-blue);
  }
  .brand-name {
    font-family: "Open Sans", sans-serif; font-weight: 700;
    font-size: 74px; color: var(--brand-blue); letter-spacing: -1px;
  }
  .service-band {
    position: absolute; top: 243px; left: 0; width: 100%; height: 198px;
    background: var(--band-grey);
  }
  .service-title {
    position: absolute; top: 14px; left: 0; width: 100%; text-align: center;
    font-family: "Open Sans", sans-serif; font-weight: 700; font-size: 31px;
    color: #ffffff; letter-spacing: 1px;
  }
  .service-icon { position: absolute; top: 62px; width: 88px; height: 88px; }
  .icon-sync { left: 222px; }
  .icon-sell { left: 332px; }
  .icon-ship { left: 438px; }

  /* Back */
  .bars { position: absolute; top: 0; left: 0; }
  .contact {
    position: absolute; font-family: "Didact Gothic", sans-serif;
    color: var(--ink-soft); font-size: 25px; line-height: 1; white-space: nowrap;
  }
  .contact-name {
    font-family: "Open Sans", sans-serif; font-weight: 700; font-size: 25px;
    color: var(--ink-soft); left: 147px; top: 50px;
  }
  .contact-role { left: 147px; top: 82px; font-family: "Open Sans", sans-serif; font-size: 25px; }
  .contact-phone { left: 165px; top: 153px; }
  .contact-email { left: 178px; top: 232px; }
  .contact-web { left: 192px; top: 312px; }
  .contact-address { left: 205px; top: 379px; font-size: 22px; line-height: 27px; }
  .contact-address span { display: block; }
  .contact-address span + span { padding-left: 6px; }
</style>
</head>
<body>
<main class="canvas">

  <section class="card card-front" aria-label="Card front">
    <div class="brand">
      <span class="brand-dot"></span>
      <span class="brand-name">Qbrook718</span>
    </div>
    <div class="service-band">
      <p class="service-title">SYNC | SELL | SHIP</p>

      <svg class="service-icon icon-sync" viewBox="0 0 88 88" aria-label="Sync">
        <circle cx="44" cy="44" r="44" fill="#1a9ad6"/>
        <rect x="21" y="27" width="46" height="29" rx="2" fill="#fff"/>
        <rect x="24" y="30" width="40" height="22" fill="#1a9ad6"/>
        <rect x="24" y="30" width="40" height="22" fill="#111"/>
        <rect x="41" y="56" width="6" height="8" fill="#fff"/>
        <rect x="33" y="63" width="22" height="3" rx="1" fill="#fff"/>
      </svg>

      <svg class="service-icon icon-sell" viewBox="0 0 88 88" aria-label="Sell">
        <circle cx="44" cy="44" r="44" fill="#97c22b"/>
        <circle cx="44" cy="44" r="33" fill="#fff"/>
        <circle cx="44" cy="44" r="27" fill="none" stroke="#111" stroke-width="4"/>
        <text x="44" y="57" text-anchor="middle" font-family="Open Sans, sans-serif" font-weight="700" font-size="36" fill="#111">$</text>
      </svg>

      <svg class="service-icon icon-ship" viewBox="0 0 88 88" aria-label="Ship">
        <circle cx="44" cy="44" r="44" fill="#fff"/>
        <path d="M18 34 h12 v-6 h28 c6 0 11 4 11 10 v14 h-51 z" fill="#222"/>
        <path d="M18 34 h12 v8 h-12 z" fill="#222"/>
        <rect x="19" y="35" width="9" height="6" fill="#fff"/>
        <g stroke="#fff" stroke-width="2">
          <line x1="40" y1="33" x2="64" y2="33"/>
          <line x1="42" y1="38" x2="64" y2="38"/>
          <line x1="44" y1="43" x2="64" y2="43"/>
        </g>
        <circle cx="28" cy="54" r="5" fill="#222" stroke="#fff" stroke-width="2"/>
        <circle cx="58" cy="54" r="5" fill="#222" stroke="#fff" stroke-width="2"/>
      </svg>
    </div>
  </section>

  <section class="card card-back" aria-label="Card back">
    <svg class="bars" width="747" height="441" viewBox="0 0 747 441">
      <g fill="#97c22b">
        <polygon points="0,0 107,0 111,22 0,22"/>
        <polygon points="0,48 118,48 124,105 0,105"/>
        <polygon points="0,131 131,131 137,188 0,188"/>
        <polygon points="0,214 144,214 150,271 0,271"/>
        <polygon points="0,297 157,297 163,354 0,354"/>
        <polygon points="0,380 169,380 175,441 0,441"/>
      </g>
      <!-- person -->
      <g fill="#222" transform="translate(99 76)">
        <circle cx="0" cy="-9" r="8"/>
        <path d="M-17 17 c0-12 7-17 17-17 c10 0 17 5 17 17 z"/>
        <path d="M-2 1 h4 l2 12 -4 4 -4-4 z" fill="#97c22b"/>
      </g>
      <!-- tablet -->
      <g transform="translate(107 159)">
        <rect x="-12" y="-18" width="24" height="36" rx="3" fill="none" stroke="#222" stroke-width="3"/>
        <line x1="-12" y1="10" x2="12" y2="10" stroke="#222" stroke-width="2"/>
        <circle cx="0" cy="14" r="1.8" fill="#222"/>
      </g>
      <!-- envelope -->
      <g transform="translate(118 243)" fill="none" stroke="#222" stroke-width="3">
        <rect x="-18" y="-12" width="36" height="24" rx="2"/>
        <polyline points="-18,-12 0,3 18,-12"/>
      </g>
      <!-- globe -->
      <g transform="translate(129 326)" fill="none" stroke="#222" stroke-width="2.2">
        <circle r="16"/>
        <ellipse rx="7" ry="16"/>
        <line x1="0" y1="-16" x2="0" y2="16"/>
        <line x1="-16" y1="0" x2="16" y2="0"/>
        <path d="M-14 -8 h28 M-14 8 h28"/>
      </g>
      <!-- pin -->
      <g transform="translate(137 408)">
        <path d="M0 22 c-4-10 -13-17 -13-27 a13 13 0 0 1 26 0 c0 10 -9 17 -13 27 z" fill="#222"/>
        <circle cx="0" cy="-5" r="5" fill="#97c22b"/>
      </g>
    </svg>

    <p class="contact contact-name">Tom Haskins</p>
    <p class="contact contact-role">CEO</p>
    <p class="contact contact-phone">123-456-7888</p>
    <p class="contact contact-email">name@companyname.com</p>
    <p class="contact contact-web">www.companyname.com</p>
    <p class="contact contact-address">
      <span>2419 Pelkey Avenue</span>
      <span>J7R-2B8, Montreal, Quebec</span>
    </p>
  </section>

</main>
</body>
</html>
```